Website design for Pebble Nook Kidcare

I need a website designed for my daycare business, Pebble Nook Kidcare, now that I have a new logo. My former website was ok but simple and I did not have a logo yet. It also was created by me using a template and was entirely pink. I loved the bright, happy feel of it but worried it might not appeal as much to potential clients who have sons. Therefore, I need a site which will appeal to both genders while still keeping the cheerful color scheme of my new logo, which has pinks, blue, green and cream.
Updates

Reason: Hello! I am still trying to download my new logo and am sorry it is taking me so long. Hopefully I will it posted by the end of today (US Eastern Standard Time). Thank you all very much for your patience!

Hello! I have finally managed to upload my new logo for you to use in designing my website. I'm sorry it took so long and greatly appreciate your time and creative efforts! I look forward to seeing what is submitted based on my logo design and its style/colors.

Many thanks!

Reason: As I've been traveling and posted my logo file late, I am extending my deadline. I am now back and can focus on providing more and better feedback. I appreciate your patience and submissions very much!

Reason: I need more time to provide feedback and make decisions.

Industry/Entity Type

Daycare

Colors
0192cd
33a6d7
86cae7
cadf82
fbf289
add136
e34197

```html
<!DOCTYPE html>
<html lang="en">
<head>
<meta charset="utf-8">
<title>Pebble Nook Kidcare</title>
<link rel="stylesheet" href="https://fonts.googleapis.com/css2?family=Didact+Gothic&family=Mulish:wght@700;800&display=swap">
<style>
  :root {
    --pink: #e8629a;
    --pink-soft: #f7a9c3;
    --blue: #0192cd;
    --blue-mid: #33a6d7;
    --blue-soft: #86cae7;
    --green: #add136;
    --green-soft: #cadf82;
    --cream: #fbf289;
    --ink: #1d1d1d;
    --white: #ffffff;
    --rule: #d9d9d9;
    --photo-warm: #e9c4a4;
    --photo-teal: #3cbcc9;
    --photo-lime: #a9cf3b;
  }
  * { margin: 0; padding: 0; box-sizing: border-box; }
  html, body { width: 1200px; height: 579px; overflow: hidden; background: var(--white); }
  body { position: relative; font-family: "Didact Gothic", "Century Gothic", sans-serif; color: var(--ink); }

  .backdrop {
    position: absolute; inset: 0;
    background:
      radial-gradient(ellipse 110px 90px at 205px 40px, rgba(232,98,154,.45), transparent 70%),
      radial-gradient(ellipse 70px 80px at 195px 130px, rgba(134,202,231,.45), transparent 70%),
      radial-gradient(ellipse 140px 260px at 250px 300px, rgba(245,140,170,.30), transparent 70%),
      radial-gradient(ellipse 90px 120px at 150px 530px, rgba(202,223,130,.55), transparent 70%),
      radial-gradient(ellipse 520px 70px at 620px 420px, rgba(134,202,231,.35), transparent 70%),
      radial-gradient(ellipse 420px 50px at 640px 580px, rgba(232,98,154,.35), transparent 70%),
      radial-gradient(ellipse 120px 60px at 1030px 560px, rgba(51,166,215,.35), transparent 70%),
      radial-gradient(ellipse 90px 60px at 470px 20px, rgba(251,242,137,.5), transparent 70%),
      var(--white);
  }

  .logo-slot {
    position: absolute; left: 313px; top: 22px;
    font-family: "Mulish", sans-serif; font-weight: 800; font-size: 12px;
    color: var(--pink-soft); letter-spacing: .3px;
  }

  .main-nav {
    position: absolute; left: 286px; top: 52px; width: 640px; height: 34px;
    background: var(--white); border-bottom: 2px solid var(--blue-soft);
    display: flex; align-items: center;
  }
  .main-nav a {
    height: 100%; display: flex; align-items: center; justify-content: center;
    font-size: 15px; color: var(--pink); text-decoration: none;
    border-right: 1px solid var(--rule);
  }
  .main-nav a:nth-child(even) { color: var(--blue); }
  .main-nav a:first-child { border-left: 1px solid var(--rule); }
  .social { margin-left: auto; margin-right: 16px; display: flex; gap: 5px; }
  .social span { width: 22px; height: 22px; border-radius: 3px; display: block; }
  .social .social-a { background: var(--blue-mid); }
  .social .social-b { background: var(--green); }

  .hero {
    position: absolute; left: 286px; top: 102px; width: 640px; height: 274px;
    background: var(--white); box-shadow: 0 0 2px rgba(0,0,0,.08);
  }
  .hero-photo {
    position: absolute; left: 12px; top: 14px; width: 616px; height: 246px;
    background:
      radial-gradient(ellipse 140px 120px at 340px 90px, #f1cfb0, transparent 72%),
      radial-gradient(ellipse 120px 100px at 200px 150px, #ecc7a8, transparent 72%),
      radial-gradient(ellipse 100px 80px at 520px 220px, var(--photo-lime), transparent 75%),
      radial-gradient(ellipse 120px 120px at 50px 180px, var(--photo-teal), transparent 75%),
      radial-gradient(ellipse 160px 100px at 560px 40px, var(--photo-teal), transparent 75%),
      linear-gradient(180deg, #f6ece4, var(--photo-warm));
  }
  .hero-caption {
    position: absolute; left: 12px; top: 237px; width: 616px; height: 23px;
    background: rgba(202,223,130,.45); border-top: 1px solid rgba(255,255,255,.6);
    font-family: "Mulish", sans-serif; font-weight: 800; font-size: 12px;
    color: var(--pink); padding: 5px 0 0 4px; letter-spacing: .2px;
  }

  .welcome-bar {
    position: absolute; left: 286px; top: 385px; width: 639px; height: 33px;
    background: var(--white); box-shadow: 0 1px 2px rgba(0,0,0,.12);
    border-left: 3px solid var(--blue-mid);
    font-family: "Mulish", sans-serif; font-weight: 800; font-size: 13.6px;
    color: var(--pink); padding: 8px 0 0 9px; white-space: nowrap; overflow: hidden;
  }

  .intro {
    position: absolute; left: 286px; top: 428px; width: 639px; height: 143px;
    background: var(--white); box-shadow: 0 1px 2px rgba(0,0,0,.12);
    padding: 2px 0 0 10px; font-size: 12.8px; line-height: 14.3px;
  }
</style>
</head>
<body>
  <div class="backdrop" role="img" aria-label="Soft pink, blue and green flower petals decorating the page background"></div>

  <div class="logo-slot">YOUR LOGO HERE</div>

  <nav class="main-nav">
    <a href="#" style="width:68px">Home</a>
    <a href="#" style="width:70px">About us</a>
    <a href="#" style="width:81px">Services</a>
    <a href="#" style="width:92px">Hours &amp; fees</a>
    <a href="#" style="width:69px">Contact</a>
    <a href="#" style="width:78px">Gallery</a>
    <div class="social" aria-label="Social links"><span class="social-a"></span><span class="social-b"></span></div>
  </nav>

  <section class="hero">
    <div class="hero-photo" role="img" aria-label="Photo of smiling children huddled together looking down at the camera"></div>
    <div class="hero-caption">PEBBLE NOOK KIDCARE</div>
  </section>

  <h1 class="welcome-bar">Welcome to Pebble Nook Kidcare, a playspace where children can play, create, and imagine!</h1>

  <section class="intro">
    <p>Welcome to Pebble Nook Kidcare, a licensed Group Family Day Care,<br>
    located in Brookfield's beautiful Hillcrest district. We are located on a pretty,<br>
    tree-lined block on Linden Row, between Oak and Maple Lanes.<br>
    We are a few blocks from the Green Line tram and the Harbor Road bus route,<br>
    and we offer flexible hourly childcare,<br>
    making it as easy as possible for busy parents<br>
    on the go to arrange their children's care.<br>
    We invite you to learn more about us and hope you will visit us soon!</p>
  </section>
</body>
</html>
```